Enterprise IT illustration needs a twist and uniquness

The attached Powerpoint shows four conceptual houses that consist of 5 / 6 building blocks. We will build a lot of content around this concept and want a design that looks crisp, in line with our brand colors guideline and with logo/ copyright embedded. Each building blocks should have unique color aligned with brand guideline so that content can easily aligned with the specific building block (by color). Look for a clean, modern design with a twist. Need the files also in formats where I can change text if needed at a later point.

```html
<!DOCTYPE html>
<html lang="en">
<head>
<meta charset="utf-8">
<title>kavlo – Building Blocks House</title>
<link href="https://fonts.googleapis.com/css2?family=Poppins:wght@500;600&display=swap" rel="stylesheet">
<style>
  :root {
    --roof: #f5a300;
    --action: #3b4b9c;
    --alerting: #2cbcd8;
    --correlate: #d99f1f;
    --topology: #dc4a5c;
    --harvest: #d2bf17;
    --dashboards: #121212;
    --frame: #ffffff;
    --gap: #ffffff;
    --logo-dot: #f5a300;
  }
  html, body {
    margin: 0;
    padding: 0;
    width: 977px;
    height: 1200px;
    overflow: hidden;
    background: var(--gap);
    font-family: "Poppins", sans-serif;
  }
  .canvas {
    position: relative;
    width: 977px;
    height: 1200px;
  }
  .panel {
    position: absolute;
    left: 0;
    width: 977px;
    height: 550px;
    overflow: hidden;
  }
  .panel--office { top: 0; }
  .panel--meeting { top: 650px; }
  .panel__backdrop {
    position: absolute;
    inset: 0;
  }
  .panel--office .panel__backdrop {
    background: linear-gradient(100deg, #6d4a4a 0%, #b9b3ae 28%, #d9dcdf 55%, #a9bccf 80%, #dfe3e6 100%);
  }
  .panel--meeting .panel__backdrop {
    background: linear-gradient(100deg, #3e4047 0%, #6d7177 30%, #8d9096 55%, #5a5f68 75%, #b79a8b 100%);
  }
  .brand {
    position: absolute;
    left: 37px;
    top: 34px;
    display: flex;
    align-items: center;
    gap: 12px;
    color: #ffffff;
    font-weight: 500;
    font-size: 40px;
    line-height: 1;
    letter-spacing: 1px;
  }
  .brand__dot {
    width: 30px;
    height: 30px;
    border-radius: 50%;
    background: var(--logo-dot);
  }
  .house {
    position: absolute;
    inset: 0;
    width: 977px;
    height: 550px;
  }
  .house text {
    font-family: "Poppins", sans-serif;
    font-weight: 500;
    fill: #ffffff;
  }
  .block-label { font-size: 30px; }
  .badge-num { font-size: 26px; font-weight: 600; text-anchor: middle; }
  .dash-label { font-size: 18px; font-weight: 600; letter-spacing: 1px; }
</style>
</head>
<body>
<div class="canvas">

  <!-- House with five building blocks -->
  <section class="panel panel--office">
    <div class="panel__backdrop" role="img" aria-label="Photo of two smiling colleagues in a bright office"></div>
    <div class="brand"><span class="brand__dot"></span>kavlo</div>
    <svg class="house" viewBox="0 0 1280 720" aria-label="Five building blocks house">
      <polyline points="262,228 720,82 1013,233" fill="none" stroke="var(--roof)" stroke-width="22" stroke-linecap="round" stroke-linejoin="round"/>
      <polygon points="352,218 720,113 944,224 944,303 352,303" fill="var(--action)" fill-opacity="0.85" stroke="var(--frame)" stroke-width="9" stroke-linejoin="round"/>
      <circle cx="393" cy="265" r="23" fill="#fff"/>
      <text class="badge-num" x="393" y="275" style="fill:var(--action)">5</text>
      <text class="block-label" x="432" y="275">Taking ACTION</text>

      <rect x="352" y="321" width="592" height="78" fill="var(--alerting)" fill-opacity="0.92" stroke="var(--frame)" stroke-width="9"/>
      <circle cx="393" cy="360" r="23" fill="#fff"/>
      <text class="badge-num" x="393" y="370" style="fill:var(--alerting)">4</text>
      <text class="block-label" x="432" y="371">Business Relevant Alerting</text>

      <rect x="352" y="416" width="287" height="127" fill="var(--correlate)" fill-opacity="0.92" stroke="var(--frame)" stroke-width="9"/>
      <circle cx="393" cy="480" r="23" fill="#fff"/>
      <text class="badge-num" x="393" y="490" style="fill:var(--correlate)">2</text>
      <text class="block-label" x="432" y="475">Learn &amp;</text>
      <text class="block-label" x="432" y="508">Correlate</text>

      <rect x="656" y="416" width="288" height="127" fill="var(--topology)" fill-opacity="0.92" stroke="var(--frame)" stroke-width="9"/>
      <circle cx="696" cy="480" r="23" fill="#fff"/>
      <text class="badge-num" x="696" y="490" style="fill:var(--topology)">3</text>
      <text class="block-label" x="736" y="475">Topology</text>
      <text class="block-label" x="736" y="508">Discovery</text>

      <rect x="352" y="560" width="592" height="80" fill="var(--harvest)" fill-opacity="0.92" stroke="var(--frame)" stroke-width="9"/>
      <circle cx="393" cy="600" r="23" fill="#fff"/>
      <text class="badge-num" x="393" y="610" style="fill:var(--harvest)">1</text>
      <text class="block-label" x="432" y="612">Quality DATA Harvesting</text>
    </svg>
  </section>

  <!-- House with five building blocks plus dashboards -->
  <section class="panel panel--meeting">
    <div class="panel__backdrop" role="img" aria-label="Photo of colleagues talking in a meeting room"></div>
    <div class="brand"><span class="brand__dot"></span>kavlo</div>
    <svg class="house" viewBox="0 0 1280 720" aria-label="Building blocks house with dashboards">
      <polyline points="262,228 720,82 1013,233" fill="none" stroke="var(--roof)" stroke-width="22" stroke-linecap="round" stroke-linejoin="round"/>
      <polygon points="352,218 720,113 944,224 944,303 352,303" fill="var(--action)" fill-opacity="0.85" stroke="var(--frame)" stroke-width="9" stroke-linejoin="round"/>
      <circle cx="393" cy="265" r="23" fill="#fff"/>
      <text class="badge-num" x="393" y="275" style="fill:var(--action)">5</text>
      <text class="block-label" x="432" y="275">Taking ACTION</text>

      <rect x="352" y="320" width="512" height="80" fill="var(--alerting)" fill-opacity="0.92" stroke="var(--frame)" stroke-width="9"/>
      <circle cx="393" cy="360" r="23" fill="#fff"/>
      <text class="badge-num" x="393" y="370" style="fill:var(--alerting)">4</text>
      <text class="block-label" x="432" y="371">Business Relevant Alerting</text>

      <rect x="352" y="415" width="240" height="129" fill="var(--correlate)" fill-opacity="0.92" stroke="var(--frame)" stroke-width="9"/>
      <circle cx="393" cy="480" r="23" fill="#fff"/>
      <text class="badge-num" x="393" y="490" style="fill:var(--correlate)">2</text>
      <text class="block-label" x="432" y="475">Learn &amp;</text>
      <text class="block-label" x="432" y="508">Correlate</text>

      <rect x="608" y="415" width="256" height="129" fill="var(--topology)" fill-opacity="0.92" stroke="var(--frame)" stroke-width="9"/>
      <circle cx="648" cy="480" r="23" fill="#fff"/>
      <text class="badge-num" x="648" y="490" style="fill:var(--topology)">3</text>
      <text class="block-label" x="688" y="475">Topology</text>
      <text class="block-label" x="688" y="508">Discovery</text>

      <rect x="880" y="320" width="64" height="224" fill="var(--dashboards)" stroke="var(--frame)" stroke-width="9"/>
      <circle cx="912" cy="353" r="15" fill="#fff"/>
      <path d="M912 345 V361 M904 353 H920" stroke="var(--dashboards)" stroke-width="3.5" stroke-linecap="round"/>
      <text class="dash-label" transform="translate(905 386) rotate(90)">DASHBOARDS</text>

      <rect x="352" y="560" width="592" height="81" fill="var(--harvest)" fill-opacity="0.92" stroke="var(--frame)" stroke-width="9"/>
      <circle cx="393" cy="600" r="23" fill="#fff"/>
      <text class="badge-num" x="393" y="610" style="fill:var(--harvest)">1</text>
      <text class="block-label" x="432" y="612">Quality DATA Harvesting</text>
    </svg>
  </section>

</div>
</body>
</html>
```